"Retire With The Ashbury Trust" Book Cover Design

This book is 5.5 x. 8.5 in size. Not enough room for any writing on the spine either. About 100 pages, and 18,000 words max.
The Ashbury Trust goes back to 1930. In this book, I run scenario after scenario seeing what the best strategy was for someone to Retire With The Ashbury Trust and never run out of money. And how they MIGHT be able to use this info to build a solid retirement plan using the Ashbury Trust for themselves.
Target Market(s)
Soon-to-be and recent middle-class, married retirees.
Industry/Entity Type
Investment Advisory
Requirements
Must have
- MUST BE EYE CATCHING!
Should not have
- No Piggy Banks or old people sitting on a beach or any yachts.

```html
<!DOCTYPE html>
<html lang="en">
<head>
<meta charset="utf-8">
<title>Retire With The Ashbury Trust – Book Cover</title>
<link rel="stylesheet" href="https://fonts.googleapis.com/css2?family=Bebas+Neue&family=Montserrat:wght@900&display=swap">
<style>
  :root {
    --page: #ffffff;
    --cover-dark: #1e1e1e;
    --cover-mid: #313131;
    --gold: #d4ab55;
    --gold-light: #eccf7c;
    --gold-deep: #b88a37;
    --silver: #c4c4c4;
  }
  html, body {
    margin: 0;
    padding: 0;
    width: 1200px;
    height: 1200px;
    overflow: hidden;
    background: var(--page);
  }
  .canvas {
    position: relative;
    width: 1200px;
    height: 1200px;
  }
  .cover {
    position: absolute;
    left: 254px;
    top: 64px;
    width: 722px;
    height: 1084px;
    background: radial-gradient(ellipse at 50% 45%, var(--cover-mid) 0%, #292929 55%, var(--cover-dark) 100%);
    overflow: hidden;
  }
  .subtitle {
    position: absolute;
    top: 62px;
    left: 0;
    width: 100%;
    margin: 0;
    text-align: center;
    font-family: "Bebas Neue", sans-serif;
    font-size: 36px;
    line-height: 34px;
    letter-spacing: 0.3em;
    padding-left: 0.3em;
    box-sizing: border-box;
    color: var(--gold);
    text-transform: uppercase;
  }
  .emblem {
    position: absolute;
    left: 0;
    top: 0;
    width: 722px;
    height: 1084px;
  }
  .title-arc {
    font-family: "Montserrat", sans-serif;
    font-weight: 900;
    font-size: 38px;
    text-transform: uppercase;
  }
  .tagline {
    font-family: "Bebas Neue", sans-serif;
    font-size: 27px;
    letter-spacing: 0.6em;
    text-transform: uppercase;
    fill: var(--silver);
  }
  .author {
    position: absolute;
    left: 0;
    top: 952px;
    width: 100%;
    margin: 0;
    text-align: center;
    font-family: "Bebas Neue", sans-serif;
    font-size: 98px;
    line-height: 90px;
    letter-spacing: 0.05em;
    padding-left: 0.05em;
    box-sizing: border-box;
    color: var(--gold);
  }
</style>
</head>
<body>
<div class="canvas">
  <div class="cover">
    <p class="subtitle">7 Easy Keys<br>To Make The Most Of<br>Your Retirement</p>

    <svg class="emblem" viewBox="0 0 722 1084" xmlns="http://www.w3.org/2000/svg">
      <defs>
        <linearGradient id="goldFoil" x1="0" y1="0" x2="1" y2="1">
          <stop offset="0" stop-color="var(--gold-deep)"/>
          <stop offset="0.45" stop-color="var(--gold-light)"/>
          <stop offset="1" stop-color="var(--gold)"/>
        </linearGradient>
        <radialGradient id="softGold" cx="0.5" cy="0.5" r="0.6">
          <stop offset="0" stop-color="var(--gold)" stop-opacity="0.45"/>
          <stop offset="1" stop-color="var(--gold-deep)" stop-opacity="0.15"/>
        </radialGradient>
        <path id="titlePath" d="M 119 602 A 248 248 0 1 1 605 602"/>
      </defs>

      <text class="title-arc" fill="url(#goldFoil)">
        <textPath href="#titlePath" startOffset="50%" text-anchor="middle" textLength="860" lengthAdjust="spacing">Retire With The Ashbury Trust</textPath>
      </text>

      <rect class="illustration-upper" x="234" y="417" width="262" height="113" rx="10"
            fill="url(#softGold)" role="img" aria-label="Gold foil illustration area above the tagline"/>

      <text class="tagline" x="365" y="610" text-anchor="middle">Your Own Story</text>

      <rect class="illustration-lower" x="84" y="639" width="553" height="213" rx="12"
            fill="url(#softGold)" role="img" aria-label="Gold foil illustration of a person relaxing, set below the tagline"/>
    </svg>

    <p class="author">AUTHOR NAME</p>
  </div>
</div>
</body>
</html>
```